Safety Consultancy focusing on developing exceptional Safety Leaders

I need a full but simple, modern, catchy website to drive business - my focus is on helping organizations to understand the impact that leaders have on safety performance and how they build the processes to make that happen. I already have great branding (logos) built through PixelGuild and can provide all narrative to build out the pages

Target Market(s)

Focused internationally. Typical client has a fairly robust and mature safety culture yet lacks the focused effort to develop all levels of leadership in terms of managing safety. Exercising these competencies results in continued development of an organizations safety culture as well as improved safety performance

Industry/Entity Type

all

Coding

Coded - Design and coding required

Number of Pages Required

4 page

Font styles to use
Other font styles liked:
• to match my branding

Colors
0054AA
0677BA
7BADD7
CADEEF
E8F1F8

Requirements
Must have
• Must utilize my current branding, logo, etc. I want to have a page outlining clearly my vision - which I will add to my uploads as we move forward. I need to have a page listing my extensive and unique experience as well as successes
Nice to have
• Want to leave it up to designers - but needs to be simple and easily navigable - hope to have a resource page that I can update myself with safety resource info, reports, etc.

```html
<!DOCTYPE html>
<html lang="en">
<head>
<meta charset="UTF-8">
<title>Halvorsen Safety Group</title>
<link href="https://fonts.googleapis.com/css2?family=Poppins:wght@600;700;800&family=Montserrat:wght@400;500;600;700&display=swap" rel="stylesheet">
<style>
:root{
  --navy:#2b3392;
  --indigo:#3a40a3;
  --lavender:#8e94e0;
  --pale:#eceef8;
  --ink:#111;
  --text:#333;
  --white:#fff;
}
*{margin:0;padding:0;box-sizing:border-box}
html,body{width:1200px;height:3226px;overflow:hidden}
body{position:relative;font-family:Montserrat,sans-serif;color:var(--text);background:var(--white)}
.abs{position:absolute}
.heading{font-family:Poppins,sans-serif;font-weight:800;color:var(--ink)}
.accent{color:var(--navy)}
.brand-name{font-family:Poppins,sans-serif;font-weight:700;color:var(--navy);font-size:30px;line-height:1}
.btn{display:flex;align-items:center;justify-content:center;font-weight:700;text-transform:uppercase;clip-path:polygon(6% 0,100% 0,94% 100%,0 100%)}
.btn-navy{background:var(--navy);color:var(--white)}
.btn-white{background:var(--white);color:var(--navy)}

/* hero */
.hero-photo{left:0;top:0;width:1200px;height:660px;background:linear-gradient(105deg,#4f5aa8 0%,#7d8fc4 40%,#aebfd8 65%,#c9a85a 85%,#8a97b8 100%)}
.hero-veil{left:0;top:0;width:1200px;height:660px;background:linear-gradient(90deg,rgba(58,64,163,.75) 0%,rgba(58,64,163,.35) 45%,rgba(58,64,163,0) 70%)}
.topbar{left:645px;top:0;width:555px;height:48px;background:var(--navy);clip-path:polygon(0 0,100% 0,100% 100%,6% 100%);color:var(--white);font-size:14px;display:flex;align-items:center;gap:44px;padding-left:55px}
.topbar span,.foot-contact span{display:flex;align-items:center;gap:6px}
.nav{left:523px;top:74px;display:flex;gap:31px;font-size:15px;color:#222}
.nav .active{color:var(--navy);font-weight:700;border-bottom:3px solid var(--navy);padding-bottom:12px}
.logo-header{left:108px;top:42px}
.hero-text{left:108px;top:148px;color:var(--white)}
.hero-text .welcome{font-family:Poppins,sans-serif;font-weight:700;font-size:24px}
.hero-text h1{font-family:Poppins,sans-serif;font-weight:800;font-size:62px;line-height:66px;margin-top:6px}
.hero-text p{font-size:15px;line-height:29px;width:440px;margin-top:18px}
.hero-btn{left:108px;top:476px;width:185px;height:48px;font-size:15px}

/* why */
.why-title{left:0;top:775px;width:1200px;text-align:center;font-size:40px;line-height:52px}
.arrow{width:50px;height:50px;border-radius:50%;display:flex;align-items:center;justify-content:center}
.feature{width:200px;text-align:center;font-weight:600;font-size:18px;line-height:33px;color:var(--ink)}
.feature svg{display:block;margin:0 auto 6px}

/* about */
.about{left:0;top:1155px;width:1200px;height:526px;background:var(--pale)}
.about-art{left:132px;top:1215px;width:457px;height:388px;border-radius:40px 40px 200px 40px;background:linear-gradient(135deg,#3b4e86,#c97a3a 55%,#2a3560)}
.about-title{left:641px;top:1220px;font-size:40px}
.about-copy{left:641px;top:1283px;width:405px;font-size:15.5px;line-height:30px;color:#444}
.about-btn{left:641px;top:1547px;width:186px;height:46px;font-size:15px}

/* services */
.services{left:0;top:1681px;width:1200px;height:661px;background:linear-gradient(180deg,#3a40a3,#434ab0)}
.services-title{left:0;top:1758px;width:1200px;text-align:center;color:var(--white);font-size:40px}
.card{top:1836px;width:231px;height:406px;background:var(--white);border-radius:4px;text-align:center}
.card .photo{margin:5px;height:168px;border-radius:2px}
.card h3{font-family:Montserrat,sans-serif;font-weight:700;font-size:17.5px;line-height:29px;color:var(--ink);margin-top:10px}
.card p{font-size:15.5px;line-height:30px;color:#555;margin-top:2px}
.card .btn{width:134px;height:32px;font-size:12px;margin:14px auto 0}

/* contact */
.contact-left{left:0;top:2342px;width:600px;height:623px;background:linear-gradient(160deg,#6b74d8,#4d55c0 60%,#8a7fc8)}
.contact-right{left:600px;top:2342px;width:600px;height:623px;background:#e8eaf6}
.feel{left:104px;top:2455px;color:var(--white);font-size:40px;line-height:52px}
.c-row{left:112px;display:flex;align-items:flex-start;gap:20px;color:var(--white);font-weight:600;font-size:19px;line-height:27px}
.c-ring{width:60px;height:60px;border-radius:50%;border:4px solid var(--white);display:flex;align-items:center;justify-content:center;flex:none}
.contact-title{left:600px;top:2420px;width:600px;text-align:center;font-size:40px}
.field{background:var(--white);border:1px solid #dde0ee;border-radius:6px;font-size:13px;color:#666;padding:22px 13px 0}
.submit{left:757px;top:2825px;width:190px;height:47px;font-size:16px}

/* footer */
.footer{left:0;top:2965px;width:1200px;height:261px;background:linear-gradient(180deg,#f4f4f8,#fff 30%)}
.logo-footer{left:104px;top:3066px}
.foot-nav{left:534px;top:3040px;display:flex;gap:31px;font-size:15px;color:#222}
.foot-contact{left:708px;top:3097px;display:flex;gap:44px;font-size:14px;color:var(--navy)}
.copy{left:108px;top:3160px;font-size:13.5px;line-height:27px;color:#333}
.follow{left:797px;top:3172px;font-family:Montserrat,sans-serif;font-weight:600;font-size:21px;color:var(--navy)}
.social{top:3166px;width:34px;height:34px;border-radius:50%;background:#111}
</style>
</head>
<body>

<!-- hero -->
<div class="abs hero-photo" role="img" aria-label="Safety engineer in hard hat and vest holding a radio and laptop at an industrial plant"></div>
<div class="abs hero-veil"></div>
<svg class="abs" style="left:0;top:600px" width="1200" height="100" viewBox="0 0 1200 100">
  <path d="M0 20 L600 52 L1200 20 L1200 100 L0 100Z" fill="#fff"/>
  <path d="M40 28 L600 68 L1160 28 L600 89 Z" fill="#2b3392"/>
</svg>

<div class="abs topbar">
  <span><svg width="22" height="22" viewBox="0 0 24 24"><circle cx="12" cy="12" r="10.5" fill="none" stroke="#fff" stroke-width="1.6"/><rect x="6.5" y="8" width="11" height="8" rx="1" fill="#fff"/><path d="M6.5 8.5 L12 12.5 L17.5 8.5" stroke="#2b3392" stroke-width="1.2" fill="none"/></svg>hello@halvorsensafety.example</span>
  <span><svg width="22" height="22" viewBox="0 0 24 24"><circle cx="12" cy="12" r="10.5" fill="none" stroke="#fff" stroke-width="1.6"/><path d="M8.5 7 L10.5 7 L11 9.5 L9.8 10.5 Q11 13 13.5 14.2 L14.5 13 L17 13.5 L17 15.5 Q12 17 8.5 9.5Z" fill="#fff"/></svg>1-555-014-2291</span>
</div>

<div class="abs logo-header brand-name">Halvorsen Safety Group</div>

<nav class="abs nav">
  <span class="active">HOME</span><span>ABOUT US</span><span>GUIDES</span><span>SERVICES</span><span>BLOGS</span><span>CONTACT US</span>
</nav>

<div class="abs hero-text">
  <div class="welcome">Welcome To</div>
  <h1>Halvorsen<br>Safety<br>Group</h1>
  <p>Lorem Ipsum is simply dummy text of the printing and typesetting industry. Lorem Ipsum has been the industry's</p>
</div>
<div class="abs btn btn-white hero-btn">Get Started</div>

<!-- why choose us -->
<h2 class="abs heading why-title">Why Choose Us For Your <span class="accent">Safety<br>Consultant?</span></h2>

<div class="abs arrow" style="left:33px;top:977px;background:var(--lavender)">
  <svg width="20" height="20" viewBox="0 0 20 20"><path d="M13 3 L6 10 L13 17" stroke="#fff" stroke-width="3" fill="none"/></svg>
</div>
<div class="abs arrow" style="left:1108px;top:975px;background:var(--navy)">
  <svg width="20" height="20" viewBox="0 0 20 20"><path d="M7 3 L14 10 L7 17" stroke="#fff" stroke-width="3" fill="none"/></svg>
</div>

<div class="abs feature" style="left:126px;top:928px">
  <svg width="56" height="62" viewBox="0 0 56 62"><circle cx="28" cy="22" r="13" fill="#2b3392"/><path d="M12 24 Q12 5 28 5 Q44 5 44 24" stroke="#2b3392" stroke-width="4" fill="none"/><rect x="8" y="20" width="7" height="12" rx="3" fill="#2b3392"/><rect x="41" y="20" width="7" height="12" rx="3" fill="#2b3392"/><path d="M8 60 Q8 40 28 40 Q48 40 48 60Z" fill="#2b3392"/></svg>
  Lorem Ipsum is<br>simply dummy
</div>
<div class="abs feature" style="left:375px;top:928px">
  <svg width="62" height="62" viewBox="0 0 62 62"><circle cx="31" cy="31" r="26" stroke="#2b3392" stroke-width="4" fill="none"/><circle cx="31" cy="33" r="17" fill="#2b3392"/><path d="M31 24 L31 34 L38 38" stroke="#fff" stroke-width="3" fill="none"/></svg>
  Lorem Ipsum is<br>simply dummy
</div>
<div class="abs feature" style="left:615px;top:928px">
  <svg width="58" height="62" viewBox="0 0 58 62"><path d="M29 3 L53 12 L53 30 Q53 50 29 59 Q5 50 5 30 L5 12Z" stroke="#2b3392" stroke-width="4" fill="none"/><path d="M29 11 L46 17 L46 30 Q46 45 29 51 Q12 45 12 30 L12 17Z" fill="#2b3392"/><path d="M19 31 L26 38 L40 24" stroke="#fff" stroke-width="4" fill="none"/></svg>
  Lorem Ipsum is<br>simply dummy
</div>
<div class="abs feature" style="left:864px;top:928px">
  <svg width="66" height="66" viewBox="0 0 66 66"><circle cx="33" cy="12" r="8" fill="#2b3392"/><circle cx="16" cy="36" r="6" fill="#2b3392"/><circle cx="50" cy="36" r="6" fill="#2b3392"/><path d="M33 20 L16 36 M33 20 L50 36 M16 36 L50 36" stroke="#2b3392" stroke-width="2"/><path d="M6 62 Q6 46 16 46 Q26 46 26 62Z M40 62 Q40 46 50 46 Q60 46 60 62Z" fill="#2b3392"/></svg>
  Lorem Ipsum is<br>simply dummy
</div>

<!-- about -->
<section class="abs about"></section>
<div class="abs about-art" role="img" aria-label="Letter-shaped collage of an industrial worker in a hard hat and a glowing plant at dusk"></div>
<h2 class="abs heading about-title">About <span class="accent">Us</span></h2>
<p class="abs about-copy">Lorem Ipsum is simply dummy text of the printing and typesetting industry. Lorem Ipsum has been the industry's standard dummy text ever since the 1500s, when an unknown printer took a galley of type and scrambled it to make a type specimen book. It has survived not only five centuries, but also the leap into electronic typesetting, remaining essentially unchanged.</p>
<div class="abs btn btn-navy about-btn">Get Started</div>

<!-- services -->
<section class="abs services"></section>
<h2 class="abs heading services-title">Our Safety Consultation Services</h2>

<div class="abs card" style="left:109px">
  <div class="photo" role="img" aria-label="Team of workers in hard hats on a construction site" style="background:linear-gradient(135deg,#5a4a34,#c6a04a,#3b3328)"></div>
  <h3>Lorem Ipsum is simply<br>dummy text</h3>
  <p>Lorem Ipsum is simply<br>dummy text of the<br>printing and typesetting</p>
  <div class="btn btn-navy">Read More</div>
</div>
<div class="abs card" style="left:357px">
  <div class="photo" role="img" aria-label="Inspector in orange overalls writing on a clipboard" style="background:linear-gradient(135deg,#5b7a8c,#c24a2a,#8da0ad)"></div>
  <h3>Lorem Ipsum is simply<br>dummy text</h3>
  <p>Lorem Ipsum is simply<br>dummy text of the<br>printing and typesetting</p>
  <div class="btn btn-navy">Read More</div>
</div>
<div class="abs card" style="left:607px">
  <div class="photo" role="img" aria-label="Welder in protective mask with sparks" style="background:linear-gradient(135deg,#2a3a4a,#d9783a,#2d2a2a)"></div>
  <h3>Lorem Ipsum is simply<br>dummy text</h3>
  <p>Lorem Ipsum is simply<br>dummy text of the<br>printing and typesetting</p>
  <div class="btn btn-navy">Read More</div>
</div>
<div class="abs card" style="left:855px">
  <div class="photo" role="img" aria-label="Factory worker wearing hard hat, respirator and ear protection" style="background:linear-gradient(135deg,#8ea2b4,#3d4e63,#c4cfd9)"></div>
  <h3>Lorem Ipsum is simply<br>dummy text</h3>
  <p>Lorem Ipsum is simply<br>dummy text of the<br>printing and typesetting</p>
  <div class="btn btn-navy">Read More</div>
</div>

<!-- contact -->
<div class="abs contact-left" role="img" aria-label="Smiling engineer in a hard hat and safety vest behind a blue tint"></div>
<div class="abs contact-right"></div>
<h2 class="abs heading feel" style="color:#fff">Feel Free To<br>Contact Us</h2>

<div class="abs c-row" style="top:2590px">
  <div class="c-ring"><svg width="28" height="28" viewBox="0 0 24 24"><path d="M6 3 L9 3 L10 7 L8 8.5 Q10 13 15 16 L16.5 14 L21 15 L21 18 Q12 21 6 3Z" fill="none" stroke="#fff" stroke-width="1.8"/></svg></div>
  <span style="padding-top:14px">1-555-014-2291</span>
</div>
<div class="abs c-row" style="top:2667px">
  <div class="c-ring"><svg width="26" height="30" viewBox="0 0 24 28"><path d="M12 26 Q3 15 3 10 A9 9 0 0 1 21 10 Q21 15 12 26Z" fill="none" stroke="#fff" stroke-width="2"/><circle cx="12" cy="10" r="3.5" fill="#fff"/></svg></div>
  <span style="padding-top:2px">210 Harbour View Rd, Northport,<br>Coastal Province,<br>N4K 2T9</span>
</div>
<div class="abs c-row" style="top:2766px">
  <div class="c-ring"><svg width="30" height="24" viewBox="0 0 30 24"><rect x="2" y="3" width="26" height="18" rx="2" fill="none" stroke="#fff" stroke-width="2"/><path d="M2 4 L15 14 L28 4 M2 20 L11 11 M28 20 L19 11" stroke="#fff" stroke-width="2" fill="none"/></svg></div>
  <span style="padding-top:14px">hello@halvorsensafety.example</span>
</div>

<h2 class="abs heading contact-title">Contact <span class="accent">Us</span></h2>
<div class="abs field" style="left:627px;top:2488px;width:454px;height:46px">Name</div>
<div class="abs field" style="left:627px;top:2545px;width:221px;height:46px">Phone</div>
<div class="abs field" style="left:860px;top:2545px;width:221px;height:46px">Email</div>
<div class="abs field" style="left:627px;top:2605px;width:454px;height:46px">Address</div>
<div class="abs field" style="left:627px;top:2665px;width:454px;height:122px;padding-top:20px">Message</div>
<div class="abs btn btn-navy submit">Submit</div>

<!-- footer -->
<footer class="abs footer"></footer>
<div class="abs logo-footer brand-name">Halvorsen Safety Group</div>
<nav class="abs foot-nav"><span>HOME</span><span>ABOUT US</span><span>GUIDES</span><span>SERVICES</span><span>BLOGS</span><span>CONTACT US</span></nav>
<div class="abs foot-contact">
  <span><svg width="24" height="24" viewBox="0 0 24 24"><circle cx="12" cy="12" r="10.5" fill="none" stroke="#2b3392" stroke-width="1.6"/><rect x="6.5" y="8" width="11" height="8" rx="1" fill="#2b3392"/><path d="M6.5 8.5 L12 12.5 L17.5 8.5" stroke="#fff" stroke-width="1.2" fill="none"/></svg>hello@halvorsensafety.example</span>
  <span><svg width="24" height="24" viewBox="0 0 24 24"><circle cx="12" cy="12" r="10.5" fill="none" stroke="#2b3392" stroke-width="1.6"/><path d="M8.5 7 L10.5 7 L11 9.5 L9.8 10.5 Q11 13 13.5 14.2 L14.5 13 L17 13.5 L17 15.5 Q12 17 8.5 9.5Z" fill="#2b3392"/></svg>1-555-014-2291</span>
</div>
<div class="abs copy">© 2024 Halvorsen Safety Group<br>I All Rights Reserved</div>
<div class="abs follow">FOLLOW US</div>
<div class="abs social" style="left:955px" aria-label="Social profile"></div>
<div class="abs social" style="left:1003px" aria-label="Social profile"></div>
<div class="abs social" style="left:1051px" aria-label="Social profile"></div>

</body>
</html>
```